Lumo4Kart - a fintech company - business card

We need a business card design for our Payments Technology company in Sydney, Australia. We provide business with payment solutions expanding across EFTPOS machines, online payment gateways and mobile payment solutions. We would like to see designs that are clean, classy and professional.
Target Market(s)
Business professionals, executives, c-suite
Industry/Entity Type
Fintech
Contact Information for Business Card
Will be on 400gsm. Logo will most likely be spot gloss unless designer recommends otherwise.
Font styles to use
Sans Serif
Requirements
Must have
- We need our website (lumo4kart.com.au), email (contact@lumo4kart.com.au), mobile (0432 587 904) and direct phone number (02 6815 3927) to feature on the card along with our logo (attached) and the words "EFTPOS | ONLINE | MOBILE"
- Font = Roboto

```html
<!DOCTYPE html>
<html lang="en">
<head>
<meta charset="utf-8">
<title>Lumo4Kart Business Card</title>
<link rel="stylesheet" href="https://fonts.googleapis.com/css2?family=Roboto:wght@400;700;900&family=Open+Sans:wght@400;600&display=swap">
<style>
  :root {
    --bg: #2a2b2e;
    --card-dark: #1c1d20;
    --brand-blue: #1a5f95;
    --brand-blue-light: #2470a8;
    --grey-wordmark: #6c6d70;
    --text-light: #f2f2f2;
    --divider: #55575b;
  }
  * { box-sizing: border-box; margin: 0; padding: 0; }
  html, body { width: 1200px; height: 1108px; overflow: hidden; }
  body {
    background: var(--bg);
    font-family: "Roboto", Arial, sans-serif;
    position: relative;
  }
  .card {
    position: absolute;
    top: 204px;
    width: 420px;
    height: 700px;
    border-radius: 24px;
    overflow: hidden;
    box-shadow: 0 18px 40px rgba(0,0,0,0.45);
  }
  .card-front { left: 150px; background: var(--card-dark); }
  .card-back { left: 630px; background: var(--brand-blue); }

  .brand-block {
    position: absolute;
    top: 96px; left: 0; right: 0;
    text-align: center;
  }
  .brand-dot {
    width: 150px; height: 150px;
    border-radius: 50%;
    background: var(--brand-blue);
    margin: 0 auto 28px;
  }
  .brand-name {
    font-weight: 900;
    font-size: 54px;
    letter-spacing: 0.5px;
    color: var(--grey-wordmark);
    text-transform: uppercase;
    white-space: nowrap;
  }

  .contact-block {
    position: absolute;
    top: 430px; left: 0; right: 0;
    text-align: center;
  }
  .person-name {
    font-weight: 700;
    font-size: 26px;
    color: var(--brand-blue-light);
    text-transform: uppercase;
    letter-spacing: 0.3px;
  }
  .person-title {
    font-family: "Open Sans", Arial, sans-serif;
    font-size: 19px;
    color: var(--text-light);
    margin-top: 2px;
  }
  .divider {
    width: 160px; height: 1px;
    background: var(--divider);
    margin: 14px auto 16px;
  }
  .contact-list {
    list-style: none;
    font-family: "Open Sans", Arial, sans-serif;
    font-size: 19px;
    line-height: 1.45;
    color: var(--text-light);
  }
  .contact-label { color: var(--brand-blue-light); margin-right: 4px; }
  .contact-web { color: var(--brand-blue-light); font-weight: 600; }

  .pattern-field {
    position: absolute; inset: 0;
    background: linear-gradient(180deg, #2a6ea3 0%, #1d6399 55%, var(--brand-blue) 100%);
  }
  .back-text {
    position: absolute;
    left: 40px; right: 30px; bottom: 78px;
    color: #ffffff;
  }
  .back-name {
    font-weight: 700;
    font-size: 54px;
    text-transform: uppercase;
    letter-spacing: 0.3px;
    line-height: 1;
    white-space: nowrap;
  }
  .back-tagline {
    font-size: 19px;
    letter-spacing: 0.6px;
    margin-top: 12px;
    padding-left: 4px;
    white-space: nowrap;
  }
</style>
</head>
<body>
  <section class="card card-front">
    <div class="brand-block">
      <div class="brand-dot"></div>
      <div class="brand-name">Lumo4Kart</div>
    </div>
    <div class="contact-block">
      <div class="person-name">Daniel Hartley</div>
      <div class="person-title">Managing Director</div>
      <div class="divider"></div>
      <ul class="contact-list">
        <li><span class="contact-label">M:</span>0432 587 904</li>
        <li><span class="contact-label">P:</span>02 6815 3927</li>
        <li><span class="contact-label">E:</span>contact@lumo4kart.com.au</li>
        <li class="contact-web">www.lumo4kart.com.au</li>
      </ul>
    </div>
  </section>

  <section class="card card-back">
    <div class="pattern-field" role="img" aria-label="Faint repeating brand pattern across the blue card"></div>
    <div class="back-text">
      <div class="back-name">Lumo4Kart</div>
      <div class="back-tagline">EFTPOS | ONLINE | MOBILE</div>
    </div>
  </section>
</body>
</html>
```